Business card for Quorvane, LLC

I need a business card template in .ai or similar format for my IT consultancy, Quorvane(.com)

Front side: The usual name/title/number/fax/email/contact info. Definitely san-serif, the logo font is MuseoSans 500 so the company name (Quorvane, LLC.) should definitely be in the same type and the rest of the text should be that or something complimentary. Including logo on the front is optional - I would prefer designs that include both with and without. I am open to creative input on the format.

Back side: Company logo framed somehow. I was thinking red background with the logo in a white circle in the middle, tho' I'm not sure how that would play off the red ball in the elephant's trunk. Open to creative input here too.

Attached are a (very rough) one-sided card mock-up I made, along with the logo and logo font.

```html
<!DOCTYPE html>
<html lang="en">
<head>
<meta charset="utf-8">
<title>Quorvane, LLC — Business Card</title>
<link href="https://fonts.googleapis.com/css2?family=Open+Sans:wght@400;600;800&display=swap" rel="stylesheet">
<style>
  :root {
    --stage: #2b2b2d;
    --paper: #f7f7f7;
    --brand-red: #e21d25;
    --brand-red-dark: #a8121a;
    --swoosh-grey: #3b3b3d;
    --swoosh-light: #c9c9cb;
    --ink-grey: #8a8a8a;
    --white: #ffffff;
  }
  * { margin: 0; padding: 0; box-sizing: border-box; }
  html, body {
    width: 1200px; height: 900px; overflow: hidden;
    background: var(--stage);
    font-family: "Open Sans", Arial, sans-serif;
  }
  .canvas {
    width: 1200px; height: 900px;
    display: flex; align-items: center; justify-content: center; gap: 60px;
  }
  .card {
    position: relative;
    width: 520px; height: 322px;
    overflow: hidden;
    box-shadow: 0 8px 24px rgba(0,0,0,.45);
  }
  /* Front */
  .card-front { background: var(--paper); }
  .card-front .wave { position: absolute; inset: 0; }
  .identity {
    position: absolute; top: 24px; right: 30px; text-align: right;
  }
  .identity .person-name {
    color: var(--brand-red); font-weight: 600; font-size: 20px; line-height: 1.1;
  }
  .identity .person-role {
    color: var(--ink-grey); font-size: 12.5px; margin-top: 2px;
  }
  .brand-name {
    position: absolute; left: 30px; top: 118px;
    color: var(--brand-red); font-weight: 800; font-size: 27px; letter-spacing: .5px;
  }
  .contact {
    position: absolute; right: 30px; top: 168px;
    list-style: none; text-align: right; color: var(--white);
    font-size: 12.5px; line-height: 1;
  }
  .contact li { display: flex; justify-content: flex-end; align-items: center; gap: 8px; height: 20px; }
  .contact li.gap { margin-bottom: 10px; }
  .contact .icon { width: 12px; height: 12px; flex: none; }
  .contact .spacer { width: 12px; }
  /* Back */
  .card-back {
    background: radial-gradient(circle at 50% 45%, var(--brand-red) 0%, #cf1820 55%, var(--brand-red-dark) 100%);
    display: flex; align-items: center; justify-content: center;
  }
  .emblem {
    width: 252px; height: 252px; border-radius: 50%;
    background: var(--white);
    box-shadow: 0 0 0 6px var(--brand-red), 0 0 0 8px var(--white);
    display: flex; align-items: center; justify-content: center;
  }
  .emblem .brand-name { position: static; font-size: 30px; }
</style>
</head>
<body>
<main class="canvas">
  <section class="card card-front" aria-label="Card front">
    <svg class="wave" viewBox="0 0 520 322" preserveAspectRatio="none" aria-hidden="true">
      <defs>
        <linearGradient id="redFill" x1="0" y1="0" x2="1" y2="1">
          <stop offset="0" stop-color="#f0262d"/>
          <stop offset="1" stop-color="#b0131b"/>
        </linearGradient>
      </defs>
      <path d="M0,168 C140,212 300,118 520,96 L520,112 C320,134 150,226 0,196 Z" fill="var(--swoosh-light)"/>
      <path d="M0,178 C140,222 310,128 520,104 L520,118 C320,140 150,234 0,208 Z" fill="var(--swoosh-grey)"/>
      <path d="M0,212 C150,240 330,146 520,122 L520,322 L0,322 Z" fill="url(#redFill)"/>
    </svg>

    <div class="identity">
      <p class="person-name">Your Name</p>
      <p class="person-role">Position</p>
    </div>

    <p class="brand-name">QUORVANE</p>

    <ul class="contact">
      <li><span>PO Box 1234</span><span class="spacer"></span></li>
      <li class="gap"><span>Yourcity, ST, 41101</span><span class="spacer"></span></li>
      <li><span>102 345 4646</span>
        <svg class="icon" viewBox="0 0 12 12" aria-hidden="true"><rect x="3" y="0.5" width="6" height="11" rx="1.2" fill="none" stroke="#fff" stroke-width="1.2"/><circle cx="6" cy="9.5" r=".8" fill="#fff"/></svg></li>
      <li><span>yourmail@quorvane.com</span>
        <svg class="icon" viewBox="0 0 12 12" aria-hidden="true"><rect x="0.5" y="2.5" width="11" height="7.5" fill="#fff"/><path d="M0.5,2.5 L6,7 L11.5,2.5" fill="none" stroke="#c2161e" stroke-width="1"/></svg></li>
      <li><span>www.quorvane.com</span>
        <svg class="icon" viewBox="0 0 12 12" aria-hidden="true"><g fill="none" stroke="#fff" stroke-width="1"><circle cx="6" cy="6" r="5.2"/><ellipse cx="6" cy="6" rx="2.2" ry="5.2"/><path d="M1,6 H11 M2,3.3 H10 M2,8.7 H10"/></g></svg></li>
    </ul>
  </section>

  <section class="card card-back" aria-label="Card back">
    <div class="emblem">
      <p class="brand-name">QUORVANE</p>
    </div>
  </section>
</main>
</body>
</html>
```